New company cut sheet “one page” description of services (double sided) *

Marlow Ridge Capital, LLC is looking for a newly designed one page sheet that describes the companies services. We will provide our logo and some images and content.

Target Market(s)

Companies that need to raise money or real estate owners that are looking to finance or re-finance. Raising debt and equity financing for companies looking to raise 2MM to 100MM

Industry/Entity Type

Real Estate Development

Font styles to use
Serif
Decorative

Colors

Designer to choose colors to be used in the design.

Requirements
Must have
• Logo, website, company description, why we are better. We would like some possible graphics that are regal and classy. Please list that our offices are located on Park Avenue in New York, Philadelphia, Houston and Austin
Nice to have
• Good graphics that gives the impression we are very high class and professional. Maybe a skyline or office buildings. Classy and elegant. High end business class. We are raising money for indivual projects and companies from 2MM to 100MM

```html
<!DOCTYPE html>
<html lang="en">
<head>
<meta charset="utf-8">
<title>Marlow Ridge Capital, LLC — Why Choose Us</title>
<link href="https://fonts.googleapis.com/css2?family=Playfair+Display+SC:wght@400&family=Gelasio:wght@700&family=Tinos&family=Cormorant+Garamond:wght@500&display=swap" rel="stylesheet">
<style>
  :root {
    --navy: #0b2350;
    --ivory: #ffffff;
    --frame: #e9edf4;
  }
  * { margin: 0; padding: 0; box-sizing: border-box; }
  html, body { width: 846px; height: 1200px; overflow: hidden; background: var(--navy); }
  .sheet {
    position: relative;
    width: 846px; height: 1200px;
    background: var(--navy);
    color: var(--ivory);
    overflow: hidden;
  }
  .skyline {
    position: absolute;
    top: 0; right: 0;
    width: 100px; height: 1200px;
    background: linear-gradient(90deg, var(--navy) 0%, #5d6f92 22%, #dfe4ee 45%, var(--ivory) 70%);
  }
  .contact-frame {
    position: absolute;
    left: 72px; top: 52px;
    width: 570px; height: 288px;
  }
  .contact-frame svg.frame-lines { position: absolute; inset: 0; }
  .contact-title {
    position: absolute;
    left: 0; right: 0; top: 26px;
    text-align: center;
    font-family: "Playfair Display SC", serif;
    font-weight: 400;
    font-size: 42px;
    letter-spacing: 1px;
    line-height: 1;
  }
  .contact-row {
    position: absolute;
    left: 50px;
    height: 34px;
    display: flex; align-items: center;
  }
  .contact-row svg { width: 40px; height: 34px; flex: none; }
  .contact-row span {
    margin-left: 30px;
    font-family: "Cormorant Garamond", serif;
    font-weight: 500;
    line-height: 1;
    white-space: nowrap;
  }
  .row-phone { top: 104px; }
  .row-phone span { font-size: 31px; font-family: "Playfair Display SC", serif; font-weight: 400; text-transform: lowercase; }
  .row-mail { top: 162px; }
  .row-mail span { font-size: 26px; }
  .row-web { top: 217px; }
  .row-web span { font-size: 26px; }
  .why-heading {
    position: absolute;
    left: 77px; top: 392px;
    font-family: "Gelasio", serif;
    font-weight: 700;
    font-size: 39px;
    line-height: 57px;
  }
  .why-mark {
    position: absolute;
    left: 556px; top: 392px;
    font-family: "Gelasio", serif;
    font-weight: 700;
    font-size: 125px;
    line-height: 1;
  }
  .reasons {
    position: absolute;
    left: 77px; top: 560px;
    width: 640px;
    font-family: "Tinos", serif;
    font-size: 19px;
    line-height: 24.4px;
    white-space: nowrap;
  }
  .reasons p + p { margin-top: 24px; }
</style>
</head>
<body>
<main class="sheet">
  <div class="skyline" role="img" aria-label="White city skyline silhouette along the right edge"></div>

  <section class="contact-frame">
    <svg class="frame-lines" viewBox="0 0 570 288" width="570" height="288" aria-hidden="true">
      <rect x="6" y="6" width="558" height="276" fill="none" stroke="var(--frame)" stroke-width="3"/>
      <rect x="14" y="14" width="542" height="260" fill="none" stroke="var(--frame)" stroke-width="1.2"/>
    </svg>
    <h2 class="contact-title">Contact us</h2>

    <div class="contact-row row-phone">
      <svg viewBox="0 0 40 34" aria-hidden="true">
        <path fill="var(--ivory)" d="M8 3c2-1 4 0 5 2l3 6c1 2 0 3-1 4l-2 2c2 4 5 7 9 9l2-2c1-1 2-2 4-1l6 3c2 1 3 3 2 5l-2 3c-1 1-3 2-5 1C15 31 6 22 4 11 3 8 5 5 8 3z"/>
      </svg>
      <span>0800 800 800</span>
    </div>

    <div class="contact-row row-mail">
      <svg viewBox="0 0 40 34" aria-hidden="true">
        <rect x="1" y="4" width="38" height="26" fill="var(--ivory)"/>
        <path d="M2 5l18 15L38 5M2 29l13-12M38 29L25 17" fill="none" stroke="var(--navy)" stroke-width="2"/>
      </svg>
      <span>INFO@MARLOWRIDGE.COM</span>
    </div>

    <div class="contact-row row-web">
      <svg viewBox="0 0 40 34" aria-hidden="true">
        <g fill="none" stroke="var(--ivory)" stroke-width="2.4">
          <circle cx="20" cy="17" r="15"/>
          <ellipse cx="20" cy="17" rx="6.5" ry="15"/>
          <path d="M5 17h30M7.5 9h25M7.5 25h25M20 2v30"/>
        </g>
      </svg>
      <span>WWW.MARLOWRIDGE.COM</span>
    </div>
  </section>

  <h1 class="why-heading">Why we are better<br>than our Competitors</h1>
  <div class="why-mark" aria-hidden="true">?</div>

  <section class="reasons">
    <p>We are experienced former commercial bankers who understand where<br>and how to source the very best financing arrangements for our clients.</p>
    <p>Our vast network of correspondent lenders offers regional and national<br>experience.</p>
    <p>We are commercial property owners ourselves and we treat every<br>opportunity as if it was our own.</p>
    <p>Our processes are streamlined to meet all clients’ unique needs quickly and<br>to get their projects moving forward as fast as possible.</p>
    <p>To ensure best service to our clients with no conflicts of interest, debt and<br>equity solutions are all that we do.</p>
    <p>Because we understand the vital need for privacy and data security in<br>today’s world of cyber threats, we have created our own proprietary<br>system to ensure all data is protected.</p>
    <p>Our exclusive access to high-end lenders and off-market real estate gives<br>us first shot at offering before-market incredible real estate opportunities to<br>our private investors</p>
  </section>
</main>
</body>
</html>
```